Security Special email compelling potential customers to call

I need a email designed that will go out to security dealers. A security dealer is a company that installs a security system for a homeowner to be monitored by a security company. To see the companies we are targeting go to http://www.pelmarguard.com/ or http://www.tovasentry.com/ . What we provide to these companies is the signs, aluminum stakes and decals. We want a flyer that states they can recieve free shipping on their entire order and to call for details. I have included picture files of signs and stakes That I had a professional photographer take. I have also included the last email marketing flyer we created so you could see the bones of what we want. ***NOTE*** We don't want the flyer to look like the one I have uploaded I want you to design something that will compel our target customers call us.

This program will not let me upload the hi-rez files. Please download them here: https://stickerworks.sharefile.com/d-q7ne42ffa8139b2xk

Target Market(s)

Security dealers

Industry/Entity Type

Security

Colors

Designer to choose colors to be used in the design.

Requirements
Must have
• My phone number and a compelling message
Nice to have
• Use the pictures I sent

```html
<!DOCTYPE html>
<html lang="en">
<head>
<meta charset="utf-8">
<title>The Sticker Works – Security Package Free Shipping</title>
<link rel="stylesheet" href="https://fonts.googleapis.com/css2?family=Arimo:wght@400;700&display=swap">
<style>
  :root {
    --stage: #e4e4e0;
    --paper: #ffffff;
    --ink: #231f20;
    --yellow: #fff200;
    --grey-text: #606060;
    --frame: #dcdcdc;
    --photo-top: #8f9690;
    --photo-bottom: #5f665f;
  }
  * { margin: 0; padding: 0; box-sizing: border-box; }
  html, body { width: 1200px; height: 2469px; overflow: hidden; }
  body {
    background: var(--stage);
    font-family: "Arimo", Arial, sans-serif;
    color: var(--ink);
    position: relative;
  }
  .palette {
    position: absolute; top: 72px; left: 392px;
    display: flex; align-items: center;
  }
  .palette-label { font-size: 18px; font-weight: 700; margin-right: 24px; }
  .swatch { width: 40px; height: 40px; margin-right: 11px; }
  .swatch--yellow { background: var(--yellow); }
  .swatch--black { background: var(--ink); }
  .swatch--white { background: var(--paper); }

  .email {
    position: absolute; left: 193px; top: 216px;
    width: 815px; height: 2108px;
    background: var(--paper);
    box-shadow: 0 30px 30px -20px rgba(0,0,0,0.18);
  }
  .brand {
    position: absolute; top: 44px; left: 0; width: 100%;
    text-align: center;
    font-size: 50px; font-weight: 700; color: var(--ink);
  }

  .hero { position: absolute; top: 122px; left: 0; width: 815px; height: 517px; }
  .hero-slogan {
    position: absolute; top: 433px; left: 0; width: 100%;
    text-align: center; color: var(--yellow);
    font-size: 34px; font-weight: 700;
  }

  .offer-title {
    position: absolute; top: 670px; left: 0; width: 100%;
    text-align: center; font-size: 46px; font-weight: 700;
    line-height: 58px; text-transform: uppercase; letter-spacing: 2px;
  }
  .order-button {
    position: absolute; top: 922px; left: 275px; width: 263px; height: 72px;
    background: linear-gradient(#2c2829, var(--ink));
    border-radius: 3px;
    color: var(--yellow); font-size: 23px; font-weight: 700;
    display: flex; align-items: center; justify-content: center;
    text-decoration: none;
  }
  .offer-note {
    position: absolute; top: 1020px; left: 0; width: 100%;
    text-align: center; color: var(--grey-text);
    font-size: 21px; line-height: 30px;
  }

  .call-box {
    position: absolute; top: 1129px; left: 179px; width: 458px; height: 303px;
    border: 2px solid var(--frame);
  }
  .call-title {
    position: absolute; top: 18px; left: 0; width: 100%;
    text-align: center; font-size: 37px; font-weight: 700;
  }
  .call-band { position: absolute; top: 62px; left: -12px; width: 482px; height: 146px; }
  .call-phone {
    position: absolute; top: 110px; left: 0; width: 100%;
    text-align: center; color: var(--yellow);
    font-size: 44px; font-weight: 700;
  }
  .call-question {
    position: absolute; top: 210px; left: 0; width: 100%;
    text-align: center; color: var(--grey-text);
    font-size: 21px; font-weight: 700; line-height: 30px;
  }

  .turnaround {
    position: absolute; top: 1463px; left: 0; width: 100%;
    text-align: center; font-size: 37px; line-height: 44px;
  }
  .turnaround strong { font-weight: 700; letter-spacing: 1px; }

  .site-link { position: absolute; top: 1655px; left: 224px; width: 369px; height: 90px; }
  .site-link-text {
    position: absolute; top: 52px; left: 0; width: 100%;
    text-align: center; font-size: 30px; font-weight: 700; color: var(--ink);
  }

  .footer { position: absolute; top: 1814px; left: 35px; width: 751px; height: 258px; }
  .footer-bg { position: absolute; inset: 0; }
  .social { position: absolute; top: 74px; left: 0; width: 100%; display: flex; justify-content: center; gap: 8px; }
  .social-dot { width: 40px; height: 40px; border: 2px solid #fff; border-radius: 50%; }
  .contact {
    position: absolute; top: 144px; left: 0; width: 100%;
    display: flex; justify-content: center; gap: 40px;
    color: #fff; font-size: 18px;
  }
  .contact-item { display: flex; align-items: center; gap: 10px; }
  .copyright {
    position: absolute; top: 212px; left: 0; width: 100%;
    text-align: center; color: var(--yellow);
    font-size: 16px; font-weight: 700;
  }
</style>
</head>
<body>
  <div class="palette">
    <span class="palette-label">Using Color this designs</span>
    <span class="swatch swatch--yellow"></span>
    <span class="swatch swatch--black"></span>
    <span class="swatch swatch--white"></span>
  </div>

  <main class="email">
    <header class="brand">The Sticker Works</header>

    <section class="hero">
      <svg width="815" height="517" viewBox="0 0 815 517">
        <defs>
          <linearGradient id="photo-tone" x1="0" y1="0" x2="0" y2="1">
            <stop offset="0" stop-color="#8f9690"/>
            <stop offset="1" stop-color="#5f665f"/>
          </linearGradient>
        </defs>
        <polygon points="0,74 815,0 815,354 0,411" fill="url(#photo-tone)" role="img" aria-label="Photo of a house porch with a green security yard sign on an aluminum stake"/>
        <polygon points="0,411 815,354 815,510 0,510" fill="#231f20"/>
        <rect x="0" y="510" width="815" height="7" fill="#fff200"/>
      </svg>
      <p class="hero-slogan">Serving The Security Industry Since 1983</p>
    </section>

    <h1 class="offer-title">Receive free<br>shipping on your<br>security package<br>order!</h1>
    <a class="order-button" href="#">Order Now</a>
    <p class="offer-note">Within the continental United States<br>(Minumums Apply)</p>

    <section class="call-box">
      <p class="call-title">CALL FOR DETAILS</p>
      <svg class="call-band" viewBox="0 0 482 146">
        <polygon points="0,42 482,0 482,119 0,146" fill="#231f20"/>
      </svg>
      <p class="call-phone">1-800-555-0142</p>
      <p class="call-question">Why wait 3-4 weeks for your<br>products to be produced?</p>
    </section>

    <p class="turnaround">We currently ship<br><strong>security signs &amp; decals</strong><br>in 9 working days<br>after &nbsp;PDF proof approval!</p>

    <div class="site-link">
      <svg width="369" height="90" viewBox="0 0 369 90">
        <g fill="none" stroke="#fff200" stroke-width="3">
          <polyline points="150,18 2,18 2,76 40,76"/>
          <polyline points="219,18 367,18 367,76 329,76"/>
        </g>
        <g fill="none" stroke="#231f20" stroke-width="2" stroke-linejoin="round">
          <polygon points="168,16 200,2 192,32 182,22"/>
          <line x1="200" y1="2" x2="182" y2="22"/>
        </g>
      </svg>
      <span class="site-link-text">stickerworks.com</span>
    </div>

    <footer class="footer">
      <svg class="footer-bg" width="751" height="258" viewBox="0 0 751 258">
        <polygon points="0,48 751,0 751,258 0,258" fill="#231f20"/>
      </svg>
      <div class="social">
        <span class="social-dot"></span>
        <span class="social-dot"></span>
        <span class="social-dot"></span>
      </div>
      <div class="contact">
        <span class="contact-item">
          <svg width="34" height="34" viewBox="0 0 34 34">
            <circle cx="17" cy="17" r="15" fill="none" stroke="#fff" stroke-width="2"/>
            <path d="M11 9 l4 0 l1 5 l-2 2 q2 4 5 5 l2 -2 l5 1 l0 4 q-10 1 -15 -15z" fill="#fff"/>
          </svg>
          (800) 555-0142
        </span>
        <span class="contact-item">
          <svg width="34" height="34" viewBox="0 0 34 34">
            <circle cx="17" cy="17" r="15" fill="none" stroke="#fff" stroke-width="2"/>
            <rect x="9" y="11" width="16" height="12" fill="none" stroke="#fff" stroke-width="2"/>
            <polyline points="9,11 17,18 25,11" fill="none" stroke="#fff" stroke-width="2"/>
          </svg>
          stickerworks.com
        </span>
      </div>
      <p class="copyright">Copyright 2016 The Sticker Works</p>
    </footer>
  </main>
</body>
</html>
```